Dr Mira Thalen, Orthopaedic Hand Surgeon

I am an orthopaedic hand surgeon and need business cards that reflect the surgery I do. I operate on bones, ligaments, tendons, and soft tissues. I can do microsurgery (surgery under an operating microscope) - including connecting ends of cut nerves and arteries in the fingers together. As an orthopaedic surgeon, I also fix fractures and manage orthopaedic trauma in the rest of the body. I favour black as a colour, and have some pictures of hand X-rays that you can use in the design, if you think that would look good (feel free to crop).
Updates

Hi all. Thank you for all your submissions so far. Please note that I have updated my project brief. I would like to emphasise that use of the logos that I have provided is optional, and if used, I would very much prefer the logo not to dominate the card, but add to the overall aesthetic of the card. Warm regards, Mira

Target Market(s)

Referring medical practitioners, hand therapists, patients

Industry/Entity Type

Healthcare

Contact Information for Business Card

Dr Mira Thalen
Orthopaedic Hand Surgeon
MBBS BSc (Med), MIntPH (Merit), FCWES (Ortho), FUPelV

Font styles to use
Serif

Colors

Designer to choose colors to be used in the design.

Requirements
Must have
• Space for:
• 2 addresses (a PO Box Address and a consulting suite address) - to be confirmed
• 1 phone number - to be confirmed
Nice to have
• Please choose one of the FCWES logos (I included 3 - colour, black reverse, and greyscale); if you include this in the design, IT SHOULD NOT DOMINATE THE CARD, but be smaller and more discreet.
• I have also attached the FUPelV logo (colour and greyscale); if you choose to include this in the design, IT SHOULD NOT DOMINATE THE CARD, but be smaller and more discreet.
• I would love to be able to update details on the card as time goes on, and thus would like to own the template for the card as well.
• Also I would love discussion with regard to any changes on the card, if I am not completely happy with the design, and would like to discuss things such as ease of printing, finish on the cards (matte, polish) etc.
Should not have
• I don't like the card to look too crowded

```html
<!DOCTYPE html>
<html lang="en">
<head>
<meta charset="utf-8">
<title>Dr Mira Thalen – Business Card</title>
<link rel="stylesheet" href="https://fonts.googleapis.com/css2?family=Libre+Baskerville:ital,wght@0,400;0,700;1,400&display=swap">
<style>
  :root {
    --page-bg: #2b2b2c;
    --card-bg: #343336;
    --ink-strong: #ffffff;
    --ink-main: #e6e6e6;
    --ink-soft: #b9b9bb;
    --xray-light: #d9d9db;
    --xray-mid: #8d8d90;
  }
  * { margin: 0; padding: 0; box-sizing: border-box; }
  html, body {
    width: 1200px; height: 900px; overflow: hidden;
    background: var(--page-bg);
    font-family: "Libre Baskerville", Georgia, serif;
  }
  .canvas { position: relative; width: 1200px; height: 900px; }
  .card {
    position: absolute; top: 302px;
    width: 514px; height: 296px;
    background: var(--card-bg);
    border-radius: 24px;
    overflow: hidden;
  }
  .card--back { left: 73px; }
  .card--front { left: 615px; }

  .fellowship-mark {
    position: absolute; left: 39px; top: 48px;
    display: flex; align-items: center; gap: 8px;
  }
  .fellowship-mark__square {
    width: 30px; height: 30px; background: var(--ink-strong);
  }
  .fellowship-mark__name {
    font-size: 25px; font-weight: 400; color: var(--ink-strong);
    letter-spacing: 0.5px; line-height: 1;
  }

  .hand-xray {
    position: absolute; left: 0; top: 120px;
    width: 272px; height: 168px;
    background:
      radial-gradient(ellipse 60% 42% at 55% 55%, var(--xray-light) 0%, var(--xray-mid) 45%, rgba(52,51,54,0) 100%);
    opacity: 0.85;
  }

  .details {
    position: absolute; right: 37px; top: 40px;
    text-align: right; white-space: nowrap;
  }
  .details__name {
    font-size: 16px; font-weight: 700; color: var(--ink-strong); line-height: 22px;
  }
  .details__role {
    font-size: 12px; font-style: italic; color: var(--ink-main); line-height: 20px;
  }
  .details__credentials {
    font-size: 10.5px; color: var(--ink-main); line-height: 14px; margin-top: 3px;
  }
  .details__contact {
    font-size: 12.5px; color: var(--ink-soft); line-height: 18px; margin-top: 12px;
  }
  .details__address {
    font-size: 11px; color: var(--ink-soft); line-height: 16px; margin-top: 10px;
  }
</style>
</head>
<body>
<main class="canvas">
  <section class="card card--back" aria-label="Card back"></section>

  <section class="card card--front" aria-label="Card front">
    <div class="fellowship-mark">
      <span class="fellowship-mark__square"></span>
      <span class="fellowship-mark__name">FCWES</span>
    </div>

    <div class="hand-xray" role="img" aria-label="X-ray image of an open hand showing finger and wrist bones"></div>

    <div class="details">
      <p class="details__name">Dr Mira Thalen</p>
      <p class="details__role">Orthopaedic Hand Surgeon</p>
      <p class="details__credentials">MBBS BSc (Med), MIntPH (Merit),<br>FCWES (Ortho), FUPelV</p>
      <p class="details__contact">1300 0HANDS (1300 042637)<br>doctormirathalen@handpost.com</p>
      <p class="details__address">PO Box 4812<br>Marrowvale NSW 2199</p>
      <p class="details__address">Suite 4, Level 4<br>Harbourlight Private Hospital<br>18 Wren Street, Kellmont NSW 2231</p>
    </div>
  </section>
</main>
</body>
</html>
```